Website Design for Hulls for Heroes

Please design and code a new website.
Here are the sites I like best:
http://www.wavelorn.com/alternate/
http://www.wheelsforpatriots.org
Please make it similar. This is NOT a car donation site. It's a Hulls for Heroes site. I just like this sites above as a lead generation sites.
Old site:
http://hullsforheroes.org
Updates
Coding
Coded - Design and coding required
Number of Pages Required
1 page
Look and feel

```html
<!DOCTYPE html>
<html lang="en">
<head>
<meta charset="utf-8">
<title>Hulls for Heroes — Donate Your Boat</title>
<link href="https://fonts.googleapis.com/css2?family=Nunito+Sans:wght@300;400;600;700;800&display=swap" rel="stylesheet">
<style>
:root{
  --blue:#3f63c0;
  --navy:#1f3470;
  --navy-deep:#13214a;
  --faq:#2d4676;
  --red:#b5202a;
  --orange:#ff9f2e;
  --ink:#2b2f3a;
  --muted:#555b66;
  --line:#dfe2e8;
  --white:#fff;
}
*{box-sizing:border-box;margin:0;padding:0}
html,body{width:1200px;height:3201px;overflow:hidden}
body{position:relative;font-family:"Nunito Sans",sans-serif;color:var(--ink);background:var(--white)}
.abs{position:absolute}
.site-header{left:0;top:0;width:1200px;height:85px;background:var(--white)}
.brand{left:98px;top:22px;font-size:19px;font-weight:700;letter-spacing:2px;color:var(--navy);line-height:1.1;width:110px}
.nav a{position:absolute;top:37px;font-size:11.5px;font-weight:700;color:var(--ink);text-decoration:none;letter-spacing:.3px}
.header-phone{left:862px;top:18px}
.header-phone .label{position:absolute;left:47px;top:2px;font-size:13px;color:var(--ink);white-space:nowrap}
.header-phone .number{position:absolute;left:47px;top:16px;font-size:25px;font-weight:800;color:var(--red);white-space:nowrap}
.hero-photo{left:0;top:85px;width:770px;height:555px;background:linear-gradient(180deg,#9fbfd8 0%,#c9d9e6 22%,#3f6a4d 40%,#2c5a6f 58%,#1f4f86 75%,#163f74 100%)}
.hero-form{left:770px;top:85px;width:430px;height:555px;background:var(--red)}
.hero-form h1{position:absolute;left:48px;top:40px;font-size:25px;font-weight:400;color:var(--white);line-height:1.15}
.hero-form h1 span{display:block;font-weight:700;color:var(--orange)}
.field{position:absolute;left:48px;width:284px;height:41px;background:var(--white);font-size:12px;color:#6b7180;padding:13px 17px}
.field svg{position:absolute;right:14px;top:16px}
.btn-donate{position:absolute;left:48px;top:465px;width:284px;height:47px;background:var(--orange);color:var(--white);font-size:14px;font-weight:700;text-align:center;line-height:47px}
.section-title{font-size:37px;font-weight:700;color:var(--blue);letter-spacing:.5px;white-space:nowrap}
.about-text{left:101px;top:770px;width:310px;font-size:13.5px;line-height:24.6px;color:var(--ink)}
.about-text p+p{margin-top:18px}
.link-more{font-size:13px;font-weight:700;color:var(--orange);letter-spacing:.6px}
.about-shadow{left:481px;top:709px;width:321px;height:364px;background:#dde2f2}
.about-photo{left:450px;top:690px;width:324px;height:356px;background:linear-gradient(180deg,#3d8fd1 0%,#7ab8e6 50%,#2b6aa7 62%,#174f86 100%)}
.service{position:absolute;left:851px;width:251px;height:57px;border-bottom:1px solid var(--line)}
.service svg{position:absolute;left:0;top:14px}
.service span{position:absolute;left:38px;top:20px;font-size:14px;font-weight:600}
.howto-photo{left:0;top:1292px;width:1200px;height:487px;background:linear-gradient(180deg,#e9eff4 0%,#b9cfe0 15%,#3e6fa0 30%,#2a5d93 60%,#d8e6f1 80%,#5e8ab4 100%)}
.step{position:absolute;top:1240px;width:231px;height:255px;background:linear-gradient(180deg,#233872 0%,#1d3273 70%,#27409a 100%);color:var(--white);text-align:center;padding:0 14px}
.step svg{position:absolute;left:90px;top:34px}
.step h3{position:absolute;left:0;right:0;font-size:16px;font-weight:600;line-height:22px}
.step p{position:absolute;left:14px;right:14px;font-size:11px;font-weight:300;line-height:20px;color:#dfe5f5}
.reason{position:absolute;font-size:17px;font-weight:600;color:var(--ink);line-height:21px}
.reason-icon{position:absolute}
.why-boat{left:807px;top:1900px;width:298px;height:199px;background:radial-gradient(ellipse at 55% 60%,#e8ebf0 0%,#b8bfcc 45%,#ffffff 72%)}
.faq{left:0;top:2139px;width:1200px;height:780px;background:linear-gradient(180deg,#2e4878 0%,#28416f 60%,#243a66 100%)}
.faq-title{left:0;width:1200px;top:2212px;text-align:center;font-size:37px;font-weight:700;color:var(--white);letter-spacing:.6px}
.faq-sail{left:560px;top:2139px;width:320px;height:680px;background:linear-gradient(180deg,rgba(40,60,100,0) 0%,rgba(20,36,70,.35) 50%,rgba(20,36,70,0) 100%)}
.q{position:absolute;left:177px;font-size:15px;font-weight:600;color:var(--white);white-space:nowrap}
.a{position:absolute;left:180px;top:2367px;width:400px;font-size:10.5px;line-height:15px;color:#c9d3e8}
.rule{position:absolute;left:165px;width:816px;height:1px;background:rgba(255,255,255,.22)}
.toggle{position:absolute;left:933px;width:16px;height:16px}
.site-footer{left:0;top:2919px;width:1200px;height:282px;background:var(--navy-deep);color:#c5cce0}
.foot-h{position:absolute;font-size:13px;font-weight:600;color:var(--white);letter-spacing:.4px}
.foot-l{position:absolute;font-size:11px;letter-spacing:.5px;color:#aeb7cf;white-space:nowrap;line-height:15px}
.sub-input{position:absolute;left:640px;top:151px;width:177px;height:37px;background:var(--white);font-size:9px;color:#a0a6b4;padding:13px 15px}
.sub-go{position:absolute;left:817px;top:151px;width:52px;height:37px;background:var(--red);color:var(--white);font-size:12px;font-weight:700;text-align:center;line-height:37px}
.social{position:absolute;left:995px;width:30px;height:30px;border:1.5px solid #c5cce0;border-radius:50%}
</style>
</head>
<body>

<header class="site-header abs">
  <div class="brand abs">HULLS FOR HEROES</div>
  <nav class="nav">
    <a style="left:261px">ABOUT</a>
    <a style="left:333px">HOW TO DONATE</a>
    <a style="left:466px">WHY DONATE</a>
    <a style="left:579px">FAQ</a>
  </nav>
  <div class="header-phone abs">
    <svg width="36" height="36" viewBox="0 0 36 36" fill="none" stroke="#3f63c0" stroke-width="1.8"><path d="M8 6c-3 2-4 6-1 11s9 12 14 14c4 1 7-1 8-3l-5-5-4 2c-3-1-7-6-8-9l2-4z"/><path d="M20 6a10 10 0 0 1 10 10M20 11a5 5 0 0 1 5 5"/></svg>
    <div class="label">DONATE TODAY</div>
    <div class="number">1-800-555-0147</div>
  </div>
</header>

<div class="hero-photo abs" role="img" aria-label="Sailboat on deep blue water beneath a green mountain"></div>
<section class="hero-form abs">
  <h1>Help Improve Lives.<span>Donate Your Boat Today.</span></h1>
  <div class="field" style="top:116px">Name</div>
  <div class="field" style="top:171px">Email</div>
  <div class="field" style="top:225px">Phone</div>
  <div class="field" style="top:280px">Zip Code</div>
  <div class="field" style="top:335px">Choose Year<svg width="12" height="8" viewBox="0 0 12 8"><path d="M1 1l5 5 5-5" fill="none" stroke="#9aa0ad" stroke-width="1.3"/></svg></div>
  <div class="field" style="top:389px">Choose Make<svg width="12" height="8" viewBox="0 0 12 8"><path d="M1 1l5 5 5-5" fill="none" stroke="#9aa0ad" stroke-width="1.3"/></svg></div>
  <div class="btn-donate">DONATE NOW</div>
</section>

<h2 class="section-title abs" style="left:101px;top:700px">ABOUT</h2>
<div class="about-text abs">
  <p>Lorem ipsum dolor sit amet, coctetr adcinlit pty sed diam nonmycing elit, sed diaamect continpl nibh euismod tincidunt ut lacing elit, d diaaopb eet dagna aliquam erat votpat.</p>
  <p>Lorem ipsum dolor sit amet, coctetr adipiscing inp elit, sed diam nonmy dignissim qui amect contamt landit praesent luptat vulputate velit esse molestie consequat, vel illum dolore eu feugiat nulla facilisis at vero eros.</p>
</div>
<div class="link-more abs" style="left:101px;top:1029px">READ MORE</div>
<div class="about-shadow abs"></div>
<div class="about-photo abs" role="img" aria-label="White sailboat heeling on open sea under a blue sky"></div>

<h2 class="section-title abs" style="left:871px;top:701px">SERVICES</h2>
<div class="service" style="top:769px"><svg width="30" height="28" viewBox="0 0 30 28" fill="none" stroke="#ff9f2e" stroke-width="1.5"><rect x="2" y="12" width="18" height="9"/><path d="M20 15h6l2 3v3h-8"/><circle cx="7" cy="23" r="3"/><circle cx="22" cy="23" r="3"/><path d="M4 12L14 3"/></svg><span>Sed diam nonummy</span></div>
<div class="service" style="top:826px"><svg width="30" height="28" viewBox="0 0 30 28" fill="none" stroke="#ff9f2e" stroke-width="1.5"><rect x="6" y="3" width="16" height="22" rx="2"/><path d="M10 9h8M10 14h8M10 19h5"/></svg><span>Ullamcorper suscipit lobortis</span></div>
<div class="service" style="top:883px"><svg width="30" height="28" viewBox="0 0 30 28" fill="none" stroke="#ff9f2e" stroke-width="1.5"><rect x="4" y="3" width="14" height="20"/><rect x="12" y="8" width="14" height="17"/><path d="M15 13h8M15 17h8M15 21h5"/></svg><span>Welit esse molestie consequat</span></div>
<div class="service" style="top:941px"><svg width="30" height="28" viewBox="0 0 30 28" fill="none" stroke="#ff9f2e" stroke-width="1.5"><rect x="3" y="9" width="24" height="13" rx="2"/><circle cx="9" cy="23" r="2.5"/><circle cx="21" cy="23" r="2.5"/><path d="M8 9V5h8v4M15 15h5"/></svg><span>Enim ad minim veniam</span></div>
<div class="link-more abs" style="left:889px;top:1021px">SEE ALL SERVICES</div>

<h2 class="section-title abs" style="left:0;width:1200px;text-align:center;top:1143px">HOW TO DONATES YOUR BOAT</h2>
<div class="howto-photo abs" role="img" aria-label="Motor yacht cruising fast across bright blue water with a wake"></div>
<div class="step" style="left:201px">
  <svg width="52" height="52" viewBox="0 0 52 52" fill="none" stroke="#fff" stroke-width="1.6"><circle cx="26" cy="26" r="22"/><circle cx="26" cy="22" r="8"/><path d="M12 42c3-8 8-11 14-11s11 3 14 11"/></svg>
  <h3 style="top:122px">Call us at<br>1-800-555-0147 or<br>Fill out the online form</h3>
  <p style="top:190px">Donating your vehicle is easy and donation is accepted nationwide.</p>
</div>
<div class="step" style="left:484px">
  <svg width="52" height="52" viewBox="0 0 52 52" fill="none" stroke="#fff" stroke-width="1.6"><path d="M20 6h12l-4 8h-4z"/><path d="M22 14c-9 5-12 14-8 20 3 4 20 4 23 0 4-6 1-15-9-20"/><path d="M4 44l8-6h10l6 3H18M4 44l10 4h14l16-10"/></svg>
  <h3 style="top:124px">Tax write-off</h3>
  <p style="top:155px">Once the vehicle donation is complete, you will receive your.</p>
</div>
<div class="step" style="left:768px">
  <svg width="72" height="52" viewBox="0 0 72 52" fill="none" stroke="#fff" stroke-width="1.6" style="left:80px"><rect x="4" y="24" width="40" height="14"/><path d="M44 28h14l8 6v4H44"/><circle cx="14" cy="42" r="5"/><circle cx="54" cy="42" r="5"/><path d="M8 24L30 8"/></svg>
  <h3 style="top:124px">We tow the vehicle</h3>
  <p style="top:155px">Any vehicles are accepted and we will arrange to pick up your vehicle.</p>
</div>

<h2 class="section-title abs" style="left:0;width:1188px;text-align:center;top:1828px">WHY DONATE YOUR CAR TO US</h2>
<svg class="reason-icon" style="left:104px;top:1926px" width="36" height="36" viewBox="0 0 36 36" fill="none" stroke="#ff9f2e" stroke-width="1.5"><rect x="8" y="4" width="20" height="28"/><path d="M12 12l3 3 6-6M12 22h12M12 27h8"/></svg>
<div class="reason" style="left:175px;top:1933px">IRS 501(c)3 Approved</div>
<svg class="reason-icon" style="left:94px;top:1986px" width="56" height="34" viewBox="0 0 56 34" fill="none" stroke="#ff9f2e" stroke-width="1.5"><rect x="4" y="14" width="28" height="10"/><path d="M32 17h12l6 4v3H32"/><circle cx="12" cy="27" r="4"/><circle cx="42" cy="27" r="4"/><path d="M6 14L22 3"/></svg>
<div class="reason" style="left:175px;top:1992px">Free Local Towing</div>
<svg class="reason-icon" style="left:104px;top:2046px" width="36" height="36" viewBox="0 0 36 36" fill="none" stroke="#ff9f2e" stroke-width="1.5"><rect x="6" y="4" width="20" height="28"/><path d="M10 11h12M10 16h12M10 21h8"/><circle cx="27" cy="27" r="5"/></svg>
<div class="reason" style="left:175px;top:2053px">Income Tax Deduction</div>
<svg class="reason-icon" style="left:459px;top:1926px" width="38" height="36" viewBox="0 0 38 36" fill="none" stroke="#ff9f2e" stroke-width="1.5"><circle cx="19" cy="18" r="15"/><rect x="13" y="10" width="12" height="16"/><path d="M8 8l22 20"/></svg>
<div class="reason" style="left:522px;top:1933px">No Paperwork Hassles</div>
<svg class="reason-icon" style="left:459px;top:1986px" width="38" height="38" viewBox="0 0 38 38" fill="none" stroke="#ff9f2e" stroke-width="1.5"><circle cx="19" cy="11" r="6"/><path d="M7 34c1-9 6-13 12-13s11 4 12 13z"/><path d="M19 22v12"/></svg>
<div class="reason" style="left:522px;top:1982px">Car donations help benefit<br>Harborline Foundation</div>
<svg class="reason-icon" style="left:459px;top:2046px" width="38" height="36" viewBox="0 0 38 36" fill="none" stroke="#ff9f2e" stroke-width="1.5"><rect x="4" y="12" width="22" height="16" rx="2"/><path d="M4 17h22"/><circle cx="28" cy="24" r="7"/><path d="M28 20v4h3"/></svg>
<div class="reason" style="left:522px;top:2053px">Schedule a Free Pickup</div>
<div class="why-boat abs" role="img" aria-label="White bowrider motorboat with a wakeboard tower"></div>

<section class="faq abs" aria-label="Frequently asked questions"></section>
<div class="faq-sail abs" role="img" aria-label="Silhouette of a sailboat on a misty blue sea"></div>
<h2 class="faq-title abs">FREQUENTLY ASKED QUESTIONS</h2>
<div class="q" style="top:2336px">What types of vehicles can be donated?</div>
<div class="a">We accept all vehicle donations, and in most cases, we also accept boats, motorcycles, RV's, and campers.</div>
<svg class="toggle" style="top:2340px" viewBox="0 0 16 16"><path d="M1 8h14" stroke="#fff" stroke-width="1.5"/></svg>
<div class="rule" style="top:2417px"></div>
<div class="q" style="top:2444px">Lorem Ipsum is simply dummy text of the printing and typesetting industry.</div>
<svg class="toggle" style="top:2448px" viewBox="0 0 16 16"><path d="M1 8h14M8 1v14" stroke="#fff" stroke-width="1.5"/></svg>
<div class="rule" style="top:2494px"></div>
<div class="q" style="left:181px;top:2519px">when an unknown printer took a galley of type and scrambled it</div>
<svg class="toggle" style="top:2525px" viewBox="0 0 16 16"><path d="M1 8h14M8 1v14" stroke="#fff" stroke-width="1.5"/></svg>
<div class="rule" style="top:2571px"></div>
<div class="q" style="top:2596px">with desktop publishing software like Quill PageSetter.</div>
<svg class="toggle" style="top:2602px" viewBox="0 0 16 16"><path d="M1 8h14M8 1v14" stroke="#fff" stroke-width="1.5"/></svg>
<div class="rule" style="top:2648px"></div>
<div class="q" style="top:2673px">Daniel Ashcombe, a Latin professor at Bayfield College in Virginia,</div>
<svg class="toggle" style="top:2677px" viewBox="0 0 16 16"><path d="M1 8h14M8 1v14" stroke="#fff" stroke-width="1.5"/></svg>
<div class="rule" style="top:2720px"></div>
<div class="q" style="top:2745px">Lorem Ipsum is simply dummy text of the printing and typesetting industry.</div>
<svg class="toggle" style="top:2749px" viewBox="0 0 16 16"><path d="M1 8h14M8 1v14" stroke="#fff" stroke-width="1.5"/></svg>
<div class="rule" style="top:2792px"></div>

<footer class="site-footer abs">
  <div class="foot-h" style="left:102px;top:60px">HOME</div>
  <div class="foot-l" style="left:101px;top:87px">ABOUT US</div>
  <div class="foot-l" style="left:102px;top:112px">HOW TO DONATE</div>
  <div class="foot-l" style="left:101px;top:138px">WHY DONATE</div>
  <div class="foot-l" style="left:99px;top:164px">FAQ</div>

  <div class="foot-h" style="left:294px;top:60px">CONTACT US</div>
  <svg class="abs" style="left:294px;top:97px" width="10" height="10" viewBox="0 0 10 10"><path d="M2 1l2 2-1 1c1 2 2 3 3 3l1-1 2 2-1 1C4 9 1 6 1 2z" fill="#c5cce0"/></svg>
  <div class="foot-l" style="left:320px;top:94px">1-800-555-0147</div>
  <svg class="abs" style="left:294px;top:129px" width="10" height="8" viewBox="0 0 10 8"><rect width="10" height="8" fill="#c5cce0"/><path d="M0 0l5 4 5-4" stroke="#13214a" fill="none"/></svg>
  <div class="foot-l" style="left:320px;top:126px">HELLO@HULLSFORHEROES.ORG</div>
  <svg class="abs" style="left:294px;top:162px" width="10" height="10" viewBox="0 0 10 10"><path d="M5 0a3.5 3.5 0 0 1 3.5 3.5C8.5 6 5 10 5 10S1.5 6 1.5 3.5A3.5 3.5 0 0 1 5 0z" fill="#c5cce0"/></svg>
  <div class="foot-l" style="left:320px;top:160px">HARBOR DESK<br>412 TIDEWATER LANE,<br>PORT ELLIS, MD 20977</div>

  <div class="foot-h" style="left:642px;top:60px">SUBSCRIBE TO NEWSLETTERS</div>
  <div class="foot-l" style="left:642px;top:93px;line-height:14px">GET THE LATEST NEWS AND REFRESHING<br>UPDATES DELIEVERED TO YOUR INBOX</div>
  <div class="sub-input">YOUR EMAIL</div>
  <div class="sub-go">GO</div>

  <div class="foot-h" style="left:997px;top:60px">CONNECT WITH US</div>
  <div class="social" style="top:97px"></div>
  <div class="foot-l" style="left:1046px;top:104px">DOCKSIDE SOCIAL</div>
  <div class="social" style="top:144px"></div>
  <div class="foot-l" style="left:1046px;top:151px">CHIRPLINE</div>
  <div class="social" style="top:191px"></div>
  <div class="foot-l" style="left:1046px;top:198px">PLUSBOARD</div>
</footer>

</body>
</html>
```